KP Rubbish Removal Business Card

Hey,
I need a double sided business card designed for a rubbish removal business based in Australia. Logo is already chosen, similar colours preferred for both sides of the business card.

Details to include:

Front:

KP Rubbish Removal
Darren Holloway
Managing Director
Mobile: 0471 920 246
Email: darren@kprubbishremoval.com.au
Website: kprubbishremoval.com.au

Rear:

How did we do?
kprubbishremoval.com.au/review

```html
<!DOCTYPE html>
<html lang="en">
<head>
<meta charset="UTF-8">
<title>KP Rubbish Removal – Business Card</title>
<link href="https://fonts.googleapis.com/css2?family=Montserrat:wght@400;500;600;700&display=swap" rel="stylesheet">
<style>
  :root {
    --backdrop: #3b3431;
    --card-white: #ffffff;
    --brand-green: #067312;
    --brand-green-light: #0c8a1e;
    --bright-green: #22b33a;
    --card-dark: #262626;
    --ink: #2a2a2a;
    --text-light: #ffffff;
    --text-soft: #e6efe7;
  }
  * { margin: 0; padding: 0; box-sizing: border-box; }
  html, body {
    width: 1200px; height: 716px; overflow: hidden;
    background: var(--backdrop);
    font-family: "Montserrat", Arial, sans-serif;
  }
  .canvas { position: relative; width: 1200px; height: 716px; }
  .card {
    position: absolute; top: 210px;
    width: 520px; height: 297px;
    overflow: hidden;
    box-shadow: 0 10px 28px rgba(0,0,0,.45);
  }

  /* Shared wordmark: one line, one colour, one weight */
  .brand { position: absolute; display: flex; align-items: center; }
  .brand-dot { border-radius: 50%; background: var(--brand-green); flex: none; }
  .brand-name { font-weight: 600; line-height: 1; white-space: nowrap; }

  /* Front */
  .card-front { left: 50px; background: var(--card-white); }
  .card-front .wave { position: absolute; inset: 0; }
  .card-front .brand { left: 34px; top: 86px; gap: 9px; }
  .card-front .brand-dot { width: 14px; height: 14px; }
  .card-front .brand-name { font-size: 15px; color: var(--ink); }

  .contact { position: absolute; left: 300px; top: 108px; color: var(--text-light); }
  .contact-name { font-size: 17px; font-weight: 700; letter-spacing: .2px; }
  .contact-role { font-size: 10.5px; font-weight: 500; color: var(--text-soft); margin-bottom: 12px; }
  .contact-list { list-style: none; }
  .contact-list li {
    display: flex; align-items: center; gap: 7px;
    font-size: 10.5px; line-height: 1.75; white-space: nowrap;
  }
  .contact-list svg { width: 10px; height: 10px; flex: none; }
  .icon-fill { fill: var(--text-light); }
  .icon-line { fill: none; stroke: var(--text-light); stroke-width: 2.4; }

  /* Back */
  .card-back {
    left: 630px; background: var(--card-dark);
    border-bottom: 3px solid var(--brand-green);
  }
  .card-back .brand { left: 0; right: 0; top: 104px; justify-content: center; gap: 14px; }
  .card-back .brand-dot { width: 22px; height: 22px; background: var(--bright-green); }
  .card-back .brand-name { font-size: 28px; color: var(--text-light); }

  .review { position: absolute; left: 0; right: 0; top: 212px; text-align: center; }
  .review-prompt {
    display: inline-flex; align-items: center; gap: 8px;
    color: var(--bright-green); font-size: 10.5px; font-weight: 700;
    text-transform: uppercase; letter-spacing: 1px;
  }
  .review-prompt::before, .review-prompt::after {
    content: ""; width: 18px; height: 1px; background: var(--bright-green);
  }
  .review-url { color: var(--text-light); font-size: 12px; font-weight: 500; margin-top: 4px; }
</style>
</head>
<body>
<main class="canvas">

  <section class="card card-front" aria-label="Business card front">
    <svg class="wave" viewBox="0 0 520 297" preserveAspectRatio="none" aria-hidden="true">
      <path d="M300 0 C230 40 250 190 120 297 L520 297 L520 0 Z" fill="var(--brand-green-light)"/>
      <path d="M318 0 C250 45 272 200 150 297 L520 297 L520 0 Z" fill="var(--brand-green)"/>
    </svg>

    <div class="brand">
      <span class="brand-dot"></span>
      <span class="brand-name">KP Rubbish Removal</span>
    </div>

    <div class="contact">
      <p class="contact-name">Darren Holloway</p>
      <p class="contact-role">Managing Director</p>
      <ul class="contact-list">
        <li>
          <svg viewBox="0 0 24 24" aria-hidden="true"><path class="icon-fill" d="M6.6 10.8a15 15 0 0 0 6.6 6.6l2.2-2.2a1 1 0 0 1 1-.25 11.4 11.4 0 0 0 3.6.57 1 1 0 0 1 1 1V20a1 1 0 0 1-1 1A17 17 0 0 1 3 4a1 1 0 0 1 1-1h3.5a1 1 0 0 1 1 1c0 1.25.2 2.45.57 3.57a1 1 0 0 1-.25 1z"/></svg>
          0471 920 246
        </li>
        <li>
          <svg viewBox="0 0 24 24" aria-hidden="true"><rect class="icon-line" x="2" y="5" width="20" height="14"/><path class="icon-line" d="M2 5l10 8 10-8"/></svg>
          darren@kprubbishremoval.com.au
        </li>
        <li>
          <svg viewBox="0 0 24 24" aria-hidden="true"><circle class="icon-line" cx="12" cy="12" r="9.5"/><path class="icon-line" d="M2.5 12h19M12 2.5c3 3 3 16 0 19M12 2.5c-3 3-3 16 0 19"/></svg>
          kprubbishremoval.com.au
        </li>
      </ul>
    </div>
  </section>

  <section class="card card-back" aria-label="Business card back">
    <div class="brand">
      <span class="brand-dot"></span>
      <span class="brand-name">KP Rubbish Removal</span>
    </div>
    <div class="review">
      <p class="review-prompt">How did we do?</p>
      <p class="review-url">kprubbishremoval.com.au/review</p>
    </div>
  </section>

</main>
</body>
</html>
```